【 概要 】 自社メディアに誘導する広告バナーとサムネイルデザインを募集します。 【 依頼内容 】 ・サイズ: 横 × 縦1200×628 ・作成数: 1種類×1サイズ ★サムネイル用は参考画像があります。 ・利用用途:バナー広告 【 デザインイメージ 】 ・参考デザイン:検索エンジンに引っかからないようにするため、コメントにて記載Googleドキュメントのテキストにて添付いたします。 こちらより参考にしてくださいませ。 https://notes.pelvarix.net/document/d/7Qw3LmZr8TyUbXcVnK2sDfGhJp4Ae9RoWi61Lkuvzt_P/edit?usp=sharing 【 契約金額(税抜) 】 2,000円 ※契約金額(税込)からシステム利用料を差し引いた金額が、ワーカーさまの受取金額となります その他ご質問等ありましたら、気軽にお問い合わせください。 ご応募をお待ちしております! |
| https://hibikurashi.tane-kobora.jp/localblog/rivo_kayaking.html | ||

```html
<!DOCTYPE html>
<html lang="ja">
<head>
<meta charset="utf-8">
<title>オトナの停滞肌をレスキュー！</title>
<link rel="stylesheet" href="https://fonts.googleapis.com/css2?family=Noto+Sans+JP:wght@700;900&display=swap">
<style>
  :root {
    --ink: #1f1f24;
    --rescue: #e2437c;
    --teal: #3cc3cf;
    --marker: #fff07a;
    --sparkle: #f6c93a;
    --panel: rgba(255, 255, 255, 0.93);
    --photo-left-a: #eef0f3;
    --photo-left-b: #d9dde3;
    --photo-right-a: #f4f5f6;
    --photo-right-b: #dfe3e6;
  }
  * { margin: 0; padding: 0; box-sizing: border-box; }
  html, body { width: 1200px; height: 628px; overflow: hidden; background: #fff; }
  .banner {
    position: relative;
    width: 1200px;
    height: 628px;
    overflow: hidden;
    font-family: "Noto Sans JP", sans-serif;
    color: var(--ink);
  }
  .photo { position: absolute; top: 0; height: 628px; }
  .photo--products {
    left: 0; width: 600px;
    background: linear-gradient(160deg, var(--photo-left-a) 0%, #ffffff 45%, var(--photo-left-b) 100%);
  }
  .photo--advisor {
    right: 0; width: 600px;
    background: linear-gradient(200deg, var(--photo-right-a) 0%, #ffffff 40%, var(--photo-right-b) 100%);
  }
  .panel {
    position: absolute;
    left: 330px; top: 0;
    width: 540px; height: 628px;
    background: var(--panel);
    box-shadow: 0 0 40px 30px var(--panel);
  }
  .copy {
    position: absolute;
    left: 330px; top: 0;
    width: 540px; height: 628px;
    text-align: center;
  }
  .accent-ticks { position: absolute; left: 248px; top: 26px; }
  .lead-age {
    position: absolute; left: 0; right: 0; top: 58px;
    font-size: 44px; font-weight: 900; letter-spacing: 1px;
  }
  .lead-concerns {
    position: absolute; left: 0; right: 0; top: 130px;
    font-size: 34px; font-weight: 900; letter-spacing: 1px;
  }
  .headline {
    position: absolute; left: 0; right: 0; top: 246px;
    font-size: 64px; font-weight: 900; letter-spacing: 1px;
  }
  .headline__marked {
    background: linear-gradient(transparent 62%, var(--marker) 62%, var(--marker) 92%, transparent 92%);
  }
  .headline__particle { font-size: 42px; }
  .rescue {
    position: absolute; left: 0; right: 0; top: 350px;
    font-size: 58px; font-weight: 900; color: var(--rescue); letter-spacing: 2px;
  }
  .sparkle { position: absolute; top: 364px; }
  .sparkle--left { left: 56px; }
  .sparkle--right { left: 428px; }
  .brand-tag {
    position: absolute; left: 100px; top: 468px;
    width: 340px; height: 58px;
    background: var(--teal); border-radius: 12px;
    color: #fff; font-size: 34px; font-weight: 900; line-height: 58px;
    letter-spacing: 1px;
  }
  .brand-honorific {
    position: absolute; left: 446px; top: 508px;
    font-size: 20px; font-weight: 700;
  }
  .closing {
    position: absolute; left: 0; right: 0; top: 544px;
    font-size: 34px; font-weight: 900; letter-spacing: 1px;
  }
</style>
</head>
<body>
  <div class="banner">
    <div class="photo photo--products" role="img" aria-label="白い机の上に並ぶ白と青のスキンケア化粧品ボトルと資料"></div>
    <div class="photo photo--advisor" role="img" aria-label="化粧品ブランドのショールームで案内する黒い服の女性スタッフ"></div>
    <div class="panel"></div>

    <div class="copy">
      <svg class="accent-ticks" width="44" height="24" viewBox="0 0 44 24" aria-hidden="true">
        <g stroke="#1f1f24" stroke-width="3" stroke-linecap="round">
          <line x1="6" y1="4" x2="12" y2="18"/>
          <line x1="22" y1="2" x2="22" y2="16"/>
          <line x1="38" y1="4" x2="32" y2="18"/>
        </g>
      </svg>
      <p class="lead-age">30代からの</p>
      <p class="lead-concerns">乾燥・くすみ・たるみ…</p>
      <p class="headline"><span class="headline__marked">オトナの停滞肌</span><span class="headline__particle">を</span></p>

      <svg class="sparkle sparkle--left" width="56" height="56" viewBox="0 0 56 56" aria-hidden="true">
        <path fill="var(--sparkle)" d="M34 6 L38 22 L52 26 L38 30 L34 46 L30 30 L16 26 L30 22 Z"/>
        <path fill="var(--sparkle)" d="M12 34 L14 42 L22 44 L14 46 L12 54 L10 46 L2 44 L10 42 Z"/>
      </svg>
      <p class="rescue">レスキュー！</p>
      <svg class="sparkle sparkle--right" width="56" height="56" viewBox="0 0 56 56" aria-hidden="true">
        <path fill="var(--sparkle)" d="M22 6 L26 22 L40 26 L26 30 L22 46 L18 30 L4 26 L18 22 Z"/>
        <path fill="var(--sparkle)" d="M44 34 L46 42 L54 44 L46 46 L44 54 L42 46 L34 44 L42 42 Z"/>
      </svg>

      <div class="brand-tag">ハルノエ化粧品</div>
      <span class="brand-honorific">さん</span>
      <p class="closing">に聞いてみた！</p>
    </div>
  </div>
</body>
</html>
```